'Tarnby Electrical' web design

I need a web design for an electrical/electrician company based in sydney called tarnby electrical. The logo design and business card design have been uploaded to be used on the web design. I want the design to be very modern and clean. I want the sector designs on the business card, i.e "residential", "commercial" etc, to be fleshed out on the front page. Base those sector designs off the business card but try to make them more minimal and modern to suit the website. Contact details are also on the business card. Try to suit the colour scheme of the logo. The sector designs should be up the top and linked so when clicked it will scroll down the website to brief descriptions of the work the company does in those sectors. I want the website to mainly attract builders, insurance companies and the commercial sector. I want the website to look unique. Custom graphics would be nice to make the website standout. I don't want the website to look like generic.

Target Market(s)

Builders, commercial sector, home owners

Industry/Entity Type

Electrical/Construction

Coding

Coded - Design and coding required

Number of Pages Required

3 page

Requirements
Must have
• Modern design
Nice to have
• Custom graphics that make the website unique

```html
<!DOCTYPE html>
<html lang="en">
<head>
<meta charset="utf-8">
<title>Tarnby Electrical</title>
<link href="https://fonts.googleapis.com/css2?family=Montserrat:wght@400;500;600;700&display=swap" rel="stylesheet">
<style>
:root{
  --blue:#1553a9;
  --blue-dark:#0f3f85;
  --navy:#1e3157;
  --orange:#f07f3c;
  --ink:#1b1b1b;
  --muted:#555;
  --grey-bg:#f2f3f5;
  --footer:#2b2b2b;
  --white:#fff;
}
*{box-sizing:border-box;margin:0;padding:0}
html,body{width:1200px;height:5269px;overflow:hidden}
body{font-family:'Montserrat',sans-serif;color:var(--ink);background:var(--white);position:relative}
section,header,footer{position:absolute;left:0;width:1200px}
.abs{position:absolute}
.eyebrow{font-size:14px;text-transform:uppercase;letter-spacing:.5px;color:#333}
.h2{font-size:32px;font-weight:700;color:var(--ink)}
.center{text-align:center;width:100%}
.btn{position:absolute;background:var(--orange);color:#fff;font-weight:600;font-size:17px;display:flex;align-items:center;justify-content:center;gap:10px;border-radius:2px}
.placeholder{position:absolute}
.logo{display:flex;align-items:center;gap:10px;font-weight:700;font-size:24px;color:var(--blue)}
.logo i{display:block;width:26px;height:26px;background:var(--orange)}

/* header */
.site-header{top:0;height:92px}
.nav{left:525px;top:40px;display:flex;gap:24px;font-size:15px;color:#222}
.call{left:985px;top:30px;display:flex;gap:12px;align-items:center}
.call small{display:block;font-size:12px;color:#666}
.call b{font-size:17px;color:var(--blue)}

/* hero */
.hero{top:92px;height:608px}
.hero-title{left:153px;top:178px;width:560px;font-size:38px;line-height:50px;font-weight:700;color:#fff;text-transform:uppercase}
.hero-text{left:153px;top:340px;width:500px;font-size:17px;line-height:25px;color:#fff}

/* services */
.services{top:760px;height:600px}
.card{position:absolute;top:135px;width:308px;height:370px;background:#fff;box-shadow:0 2px 10px rgba(0,0,0,.1);text-align:center}
.card .photo{position:absolute;left:0;top:0;width:100%;height:200px}
.card .hex{position:absolute;left:126px;top:170px}
.card h3{position:absolute;top:245px;width:100%;font-size:20px;font-weight:700}
.card p{position:absolute;top:280px;left:20px;right:20px;font-size:13px;line-height:20px;color:var(--muted)}
.card.active{top:115px;height:417px;background:var(--blue)}
.card.active .hex{top:120px}
.card.active h3{top:195px;color:#fff}
.card.active p{top:228px;color:#dfe8f7}

/* welcome */
.welcome{top:1390px;height:531px}
.welcome-panel{left:112px;top:0;width:500px;height:531px;background:var(--blue);clip-path:polygon(0 0,100% 0,100% 88%,72% 100%,0 100%)}
.welcome-photo{left:612px;top:0;width:588px;height:531px;clip-path:polygon(0 0,100% 0,100% 100%,0 88%)}
.welcome-text{left:172px;top:80px;width:400px;color:#fff}
.welcome-text h2{font-size:32px;font-weight:700;margin:6px 0 28px}
.welcome-text p{font-size:13px;line-height:21px;color:#e6edf8}
.welcome-text ul{list-style:none;margin:18px 0}
.welcome-text li{font-size:13px;font-weight:600;margin-bottom:14px;display:flex;gap:12px;align-items:center}
.welcome-text li i{width:14px;height:14px;border:2px solid var(--orange);display:block}

/* what we do */
.what{top:1990px;height:620px}
.what-para{left:215px;top:100px;width:770px;font-size:14px;line-height:22px;color:#333;text-align:center}
.what-photo{left:112px;top:218px;width:504px;height:329px}
.steps{left:681px;top:218px;width:410px}
.steps h3{font-size:19px;font-weight:700;margin-bottom:24px}
.step{display:flex;gap:18px;margin-bottom:22px}
.step span{flex:0 0 28px;height:28px;border-radius:50%;background:var(--orange);color:#fff;font-size:12px;font-weight:600;display:flex;align-items:center;justify-content:center}
.step b{display:block;font-size:13px;margin-bottom:6px}
.step p{font-size:11px;line-height:16px;color:#444}

/* achievements */
.achieve{top:2686px;height:431px;background:linear-gradient(180deg,#2a3f68,#1a2b4e);clip-path:polygon(0 0,100% 0,100% 100%,40% 92%,30% 100%,0 100%)}
.stat{position:absolute;top:240px;width:250px;text-align:center;color:#fff}
.stat svg{display:block;margin:0 auto 20px}
.stat b{display:block;font-size:32px;font-weight:700}
.stat small{font-size:14px;text-transform:uppercase}

/* testimonials */
.testi{top:3117px;height:654px;background:var(--grey-bg)}
.rating{right:112px;top:186px;font-size:14px;display:flex;gap:10px;align-items:center}
.rating .stars{color:#f5b70a;letter-spacing:2px}
.rating b{color:var(--blue)}
.review{position:absolute;top:243px;width:308px;height:197px;background:#fff;padding:40px 22px 0}
.review p{font-size:13px;line-height:21px;color:#444}
.review .badge{position:absolute;right:20px;top:14px;width:16px;height:16px;border-radius:50%;background:#d8dce3}
.person{position:absolute;top:445px;width:308px;text-align:center;font-size:15px}
.person .avatar{width:48px;height:48px;border-radius:50%;background:linear-gradient(135deg,#f2a064,#c97a4a);border:3px solid var(--orange);margin:0 auto 8px}
.person small{display:block;font-size:13px;color:#555}
.dots{left:570px;top:566px;display:flex;gap:5px}
.dots i{display:block;width:6px;height:4px;background:#bbb}
.dots i:first-child{width:24px;background:var(--blue)}

/* projects */
.projects{top:3840px;height:480px}
.proj-side{top:145px;width:218px;height:255px}
.proj-main{left:335px;top:105px;width:563px;height:331px;box-shadow:0 6px 20px rgba(0,0,0,.3)}
.proj-caption{left:378px;top:338px;width:480px;color:#fff}
.proj-caption b{font-size:17px;display:block;margin-bottom:10px}
.proj-caption p{font-size:11px;line-height:16px}
.arrow{top:245px;width:40px;height:40px}

/* contact */
.contact{top:4393px;height:456px}
.map{left:0;top:0;width:529px;height:404px}
.form-box{left:529px;top:0;width:558px;height:456px;background:var(--blue);padding:50px 60px;color:#fff}
.form-box h2{font-size:32px;font-weight:700;margin:6px 0 28px}
.field{position:absolute;background:#fff;font-size:11px;color:#777;padding:14px 12px}
.form-box .eyebrow{color:#fff}

/* footer */
.site-footer{top:4797px;height:472px;background:var(--footer);color:#ddd}
.site-footer .logo{position:absolute;left:108px;top:130px;color:#fff;font-size:22px}
.foot-text{left:112px;top:190px;width:220px;font-size:11px;line-height:16px}
.socials{left:112px;top:290px;display:flex;gap:14px}
.socials i{display:block;width:24px;height:24px;border-radius:50%;background:#fff}
.fcol{top:135px;font-size:14px}
.fcol h4{font-size:12px;font-weight:700;color:#fff;text-transform:uppercase;margin-bottom:18px}
.fcol li{list-style:none;margin-bottom:13px}
.info{display:flex;gap:14px;margin-bottom:14px;font-size:11px;line-height:15px}
.info i{flex:0 0 22px;height:22px;border-radius:50%;background:var(--orange);display:block}
.info b{display:block;color:#fff;font-size:13px;margin-bottom:3px}
.copy{left:0;top:410px;width:1200px;height:62px;border-top:1px solid #444;font-size:11px;display:flex;justify-content:space-between;align-items:center;padding:0 112px}
.copy u{color:#fff}
</style>
</head>
<body>

<header class="site-header">
  <div class="abs logo" style="left:38px;top:33px"><i></i>Tarnby Electrical</div>
  <nav class="abs nav"><span>Home</span><span>About Us</span><span>Services</span><span>Projects</span><span>Contact Us</span></nav>
  <div class="abs call">
    <svg width="26" height="26" viewBox="0 0 24 24"><path d="M6.6 10.8a15 15 0 0 0 6.6 6.6l2.2-2.2a1 1 0 0 1 1-.25 11.4 11.4 0 0 0 3.6.57 1 1 0 0 1 1 1V20a1 1 0 0 1-1 1A17 17 0 0 1 3 4a1 1 0 0 1 1-1h3.5a1 1 0 0 1 1 1c0 1.25.2 2.45.57 3.57a1 1 0 0 1-.25 1z" fill="none" stroke="#f07f3c" stroke-width="1.8"/></svg>
    <div><small>Call Us Today!</small><b>(415) 555-0192</b></div>
  </div>
</header>

<section class="hero">
  <div class="placeholder" role="img" aria-label="Electrician in hard hat and safety glasses testing a switchboard with a multimeter" style="inset:0;background:linear-gradient(90deg,#1c2430 0%,#2f3b4a 45%,#6a7888 75%,#9aa6b2 100%)"></div>
  <h1 class="abs hero-title">Commercial and residential electrician services</h1>
  <p class="abs hero-text">Lorem ipsum dolor sit amet consectetur. Fusce mauris eget vehicula viverra.</p>
  <div class="btn" style="left:153px;top:423px;width:300px;height:52px">Request An Appointment
    <svg width="14" height="20" viewBox="0 0 14 20"><path d="M9 0 1 11h5l-2 9 9-12H8z" fill="#fff"/></svg></div>
</section>

<section class="services">
  <div class="eyebrow center abs" style="top:22px">Services</div>
  <h2 class="h2 center abs" style="top:52px">The Best Services We Provide</h2>

  <div class="card" style="left:112px">
    <div class="photo" role="img" aria-label="Close-up of hands wiring a residential terminal block" style="background:linear-gradient(135deg,#5f6a78,#a9b0b8,#3e5a8c)"></div>
    <svg class="hex" width="56" height="62" viewBox="0 0 56 62"><polygon points="28,0 56,15 56,47 28,62 0,47 0,15" fill="#f07f3c"/><path d="M18 36 28 26 38 36v8H18z" fill="none" stroke="#fff" stroke-width="2.5"/></svg>
    <h3>Residential</h3>
    <p>Lorem ipsum dolor sit amet, consectetur adipiscing elit pharetra faucibus fames sed ligula</p>
  </div>

  <div class="card active" style="left:446px">
    <div class="photo" role="img" aria-label="Office ceiling with hanging light fittings in blue tones" style="height:190px;background:linear-gradient(180deg,#8aa6cf,#2e63b1)"></div>
    <svg class="hex" width="56" height="62" viewBox="0 0 56 62"><polygon points="28,0 56,15 56,47 28,62 0,47 0,15" fill="#f07f3c"/><path d="M20 44V24h16v20M24 29h3M29 29h3M24 34h3M29 34h3M24 39h3M29 39h3" fill="none" stroke="#fff" stroke-width="2.5"/></svg>
    <h3>Commercial</h3>
    <p>Ornare ultrices sed nisl vestibulum. In montes, eget mauris non duis nunc. Ultrices lacinia enim, a, cursus lobortis viverra. Et, nibh tortor pellentesque vestibulum dui. Ac venenatis et egestas est gravida pharetra leo convallis nec tempor eget erat</p>
    <svg class="abs" style="left:260px;top:385px" width="28" height="12" viewBox="0 0 28 12"><path d="M0 6h26M20 1l6 5-6 5" fill="none" stroke="#fff" stroke-width="2"/></svg>
  </div>

  <div class="card" style="left:779px">
    <div class="photo" role="img" aria-label="Printed circuit layout drawings on paper" style="background:linear-gradient(135deg,#eef1ea,#b9d9b5,#dfe6dd)"></div>
    <svg class="hex" width="56" height="62" viewBox="0 0 56 62"><polygon points="28,0 56,15 56,47 28,62 0,47 0,15" fill="#f07f3c"/><circle cx="28" cy="31" r="10" fill="none" stroke="#fff" stroke-width="2.5"/><path d="M30 23l-5 9h6l-4 8" fill="none" stroke="#fff" stroke-width="2"/></svg>
    <h3>Circuit Designing</h3>
    <p>Lorem ipsum dolor sit amet, consectetur adipiscing elit pharetra faucibus fames sed ligula</p>
  </div>
</section>

<section class="welcome">
  <div class="abs welcome-panel"></div>
  <div class="placeholder welcome-photo" role="img" aria-label="Two engineers in hard hats reviewing plans on a construction site" style="background:linear-gradient(135deg,#cfd8e2,#7f96ad,#3d5778)"></div>
  <div class="abs welcome-text">
    <div class="eyebrow" style="color:#fff">Welcome to</div>
    <h2>Tarnby Electrical</h2>
    <p>Lorem ipsum dolor sit amet, consectetur adipiscing elit. Pharetra faucibus fames sed ac volutpat ligula faucibus elit natoque. Ornare ultrices sed nisl vestibulum. In montes, eget mauris non duis nunc. Ultrices lacinia enim.</p>
    <ul>
      <li><i></i>Ornare ultrices sed nisl vestibulum</li>
      <li><i></i>Et, nibh tortor pellentesque vestibulum dui</li>
      <li><i></i>Pharetra faucibus fames sed</li>
    </ul>
    <p>Et, nibh tortor pellentesque vestibulum dui. Ac venenatis et egestas est gravida.</p>
    <div style="margin-top:34px;font-size:14px;font-weight:600;display:flex;gap:12px;align-items:center">Learn More
      <svg width="36" height="20" viewBox="0 0 36 20"><path d="M0 10h34" stroke="#f07f3c" stroke-width="2"/><path d="M21 0 14 11h5l-2 9 8-12h-5z" fill="#f07f3c"/></svg></div>
  </div>
</section>

<section class="what">
  <div class="eyebrow center abs" style="top:12px">What We Do</div>
  <h2 class="h2 center abs" style="top:42px">More Than Just A Electrician Company</h2>
  <p class="abs what-para">Lorem ipsum dolor sit amet, consectetur adipiscing elit. Pharetra faucibus fames sed ac volutpat ligula faucibus elit natoque. Ornare ultrices sed nisl vestibulum. In montes, eget mauris non duis nunc. Ultrices lacinia enim, a, cursus lobortis viverra. Et, nibh tortor pellentesque vestibulum dui.</p>
  <div class="placeholder what-photo" role="img" aria-label="Electrician in hard hat working on a distribution board beside a brick wall" style="background:linear-gradient(135deg,#3a3f47,#6d747d,#2b3038)"></div>
  <div class="abs steps">
    <h3>Here Is Howwe Do It</h3>
    <div class="step"><span>01</span><div><b>Ornare ultrices sed nisl vestibulum</b><p>Lorem ipsum dolor sit amet, consectetur adipiscing elit pharetra faucibus fames</p></div></div>
    <div class="step"><span>02</span><div><b>Ornare ultrices sed nisl vestibulum</b><p>Lorem ipsum dolor sit amet, consectetur adipiscing elit pharetra faucibus fames</p></div></div>
    <div class="step"><span>03</span><div><b>Ornare ultrices sed nisl vestibulum</b><p>Lorem ipsum dolor sit amet, consectetur adipiscing elit pharetra faucibus fames</p></div></div>
  </div>
  <div class="btn" style="left:683px;top:492px;width:301px;height:50px">Request An Appointment
    <svg width="14" height="20" viewBox="0 0 14 20"><path d="M9 0 1 11h5l-2 9 9-12H8z" fill="#fff"/></svg></div>
</section>

<section class="achieve" role="img" aria-label="Dimmed office interior in navy tones behind achievement figures">
  <div class="eyebrow center abs" style="top:78px;color:#fff">Achievements</div>
  <h2 class="center abs" style="top:100px;font-size:32px;font-weight:700;color:#fff;line-height:42px">We Provide The&nbsp; Highest Level<br>Of Service</h2>
  <div class="stat" style="left:99px;top:232px">
    <svg width="66" height="72" viewBox="0 0 66 72"><polygon points="33,0 66,18 66,54 33,72 0,54 0,18" fill="#f07f3c"/><path d="M21 40 33 29l12 11v10H21z" fill="none" stroke="#fff" stroke-width="3"/></svg>
    <b>1,203</b><small>Projects Completed</small></div>
  <div class="stat" style="left:349px;top:232px">
    <svg width="66" height="72" viewBox="0 0 66 72"><polygon points="33,0 66,18 66,54 33,72 0,54 0,18" fill="#f07f3c"/><circle cx="33" cy="36" r="12" fill="none" stroke="#fff" stroke-width="3"/><path d="M33 28v8l5 4" stroke="#fff" stroke-width="3" fill="none"/></svg>
    <b>15</b><small>Years Experience</small></div>
  <div class="stat" style="left:600px;top:232px">
    <svg width="66" height="72" viewBox="0 0 66 72"><polygon points="33,0 66,18 66,54 33,72 0,54 0,18" fill="#f07f3c"/><circle cx="33" cy="29" r="5" fill="#fff"/><circle cx="22" cy="38" r="4" fill="#fff"/><circle cx="44" cy="38" r="4" fill="#fff"/><path d="M24 50c0-7 18-7 18 0" fill="#fff"/></svg>
    <b>100+</b><small>Staff Members</small></div>
  <div class="stat" style="left:850px;top:232px">
    <svg width="66" height="72" viewBox="0 0 66 72"><polygon points="33,0 66,18 66,54 33,72 0,54 0,18" fill="#f07f3c"/><circle cx="33" cy="31" r="10" fill="none" stroke="#fff" stroke-width="3"/><path d="M26 40l-3 12 10-5 10 5-3-12" fill="none" stroke="#fff" stroke-width="3"/></svg>
    <b>25+</b><small>Awords Won</small></div>
</section>

<section class="testi">
  <div class="eyebrow abs" style="left:112px;top:150px">Testimonials</div>
  <h2 class="h2 abs" style="left:112px;top:172px">What Our Customer Say</h2>
  <div class="abs rating"><span class="stars">★★★★★</span><span>Rated <b>5.0</b> out of <b>5</b> Based on <b>999 reviews</b></span></div>

  <div class="review" style="left:112px"><i class="badge"></i><p>Lorem ipsum dolor sit amet, consectetur adipiscing elit. Scelerisque a malesuada egestas non facilisis risus id nisi, tellus. Sed pellentesque iaculis in varius velit. Eget pellentesque libero, turpis tellus nibh ut tellus.</p></div>
  <div class="review" style="left:446px"><i class="badge"></i><p>Lorem ipsum dolor sit amet, consectetur adipiscing elit. Scelerisque a malesuada egestas non facilisis risus id nisi, tellus. Sed pellentesque iaculis in varius velit. Eget pellentesque libero, turpis tellus nibh ut tellus.</p></div>
  <div class="review" style="left:779px"><i class="badge"></i><p>Lorem ipsum dolor sit amet, consectetur adipiscing elit. Scelerisque a malesuada egestas non facilisis risus id nisi, tellus. Sed pellentesque iaculis in varius velit. Eget pellentesque libero, turpis tellus nibh ut tellus.</p></div>

  <div class="person" style="left:112px"><div class="avatar" role="img" aria-label="Customer portrait"></div>Mara Lindqvist<small>Lorem ipsum</small></div>
  <div class="person" style="left:446px"><div class="avatar" role="img" aria-label="Customer portrait"></div>Mara Lindqvist<small>Lorem ipsum</small></div>
  <div class="person" style="left:779px"><div class="avatar" role="img" aria-label="Customer portrait"></div>Mara Lindqvist<small>Lorem ipsum</small></div>
  <div class="abs dots"><i></i><i></i><i></i><i></i><i></i></div>
</section>

<section class="projects">
  <div class="eyebrow center abs" style="top:12px">Projects</div>
  <h2 class="h2 center abs" style="top:38px">Our Resent Projects</h2>
  <div class="placeholder proj-side" style="left:112px;background:linear-gradient(180deg,#7da2cf,#e6e0d4)" role="img" aria-label="Modern apartment building against blue sky"></div>
  <div class="placeholder proj-side" style="left:870px;background:linear-gradient(180deg,#3f6fb2,#c7c3b8)" role="img" aria-label="Residential building under a cloudy sky"></div>
  <div class="placeholder proj-main" style="background:linear-gradient(180deg,#9a6a4e 0%,#6b4a3a 55%,#1d1a1a 100%)" role="img" aria-label="Electrician installing a switchboard in an unfinished brick room"></div>
  <div class="abs proj-caption"><b>Lorem Ipsum Dolor</b><p>Lorem ipsum dolor sit amet, consectetur adipiscing elit. Scelerisque a malesuada egestas non facilisis risus id nisi consectetur adipiscing elit</p></div>
  <svg class="abs arrow" style="left:90px" viewBox="0 0 40 40"><polygon points="20,0 40,20 20,40 0,20" fill="#f07f3c"/><path d="M28 20H12M17 15l-5 5 5 5" stroke="#fff" stroke-width="2" fill="none"/></svg>
  <svg class="abs arrow" style="left:1070px" viewBox="0 0 40 40"><polygon points="20,0 40,20 20,40 0,20" fill="#f07f3c"/><path d="M12 20h16M23 15l5 5-5 5" stroke="#fff" stroke-width="2" fill="none"/></svg>
</section>

<section class="contact">
  <div class="placeholder map" role="img" aria-label="Street map showing the office location" style="background:linear-gradient(135deg,#eceff1,#dfe4e8)"></div>
  <div class="abs form-box">
    <div class="eyebrow">Contact Us</div>
    <h2>Let Us Assist You</h2>
    <div class="field" style="left:60px;top:127px;width:215px;height:38px">Name *</div>
    <div class="field" style="left:285px;top:127px;width:213px;height:38px">Phone *</div>
    <div class="field" style="left:60px;top:196px;width:438px;height:38px">Email *</div>
    <div class="field" style="left:60px;top:250px;width:438px;height:83px">Write Message here</div>
    <div class="btn" style="left:60px;top:363px;width:154px;height:50px">Submit
      <svg width="14" height="20" viewBox="0 0 14 20"><path d="M9 0 1 11h5l-2 9 9-12H8z" fill="#fff"/></svg></div>
  </div>
</section>

<footer class="site-footer">
  <div class="logo"><i></i>Tarnby Electrical</div>
  <p class="abs foot-text">Lorem ipsum dolor sit amet, consectetur adipiscing elit pharetra faucibus fames</p>
  <div class="abs socials"><i></i><i></i><i></i><i></i></div>
  <div class="abs fcol" style="left:521px"><h4>Quick Links</h4><ul><li>Home</li><li>About Us</li><li>Services</li><li>Projects</li><li>Contact Us</li></ul></div>
  <div class="abs fcol" style="left:669px"><h4>Customer Services</h4><ul><li>Residential</li><li>Commercial</li><li>Circuit Designing</li></ul></div>
  <div class="abs fcol" style="left:874px;width:215px"><h4>Our Contact Info</h4>
    <div class="info"><i></i><div><b>Location</b>48 Harbour Lane, Millbrook, NSW 2190</div></div>
    <div class="info"><i></i><div><b>Phone</b>(415) 555-0192</div></div>
    <div class="info" style="margin-top:26px"><i></i><div><b>Mail</b>tarnby.electrical@example.com</div></div>
  </div>
  <div class="abs copy"><span>©Copyright 2022. <u>Tarnby Electrical</u> | All Rights Reserved</span><span>Privacy Policy &nbsp;|&nbsp; Terms and Conditions</span></div>
</footer>

</body>
</html>
```